velmu GmbH needs great looking businesscards to leave an impression

Dear Designers,

Our company velmu GmbH based in switzerland needs to have impressive businesscards. We produce and sell high quality bleaching products for the upper market.
We'd like to have a minimalistic but still meaningful design. You'll fine our company logo attached and some of our packaging designs. Our company slogan is "discover your smile". If you need additional information feel free to contact us.
Kind Regards Dano

Dear Designers, This is a business card design contest! I try to call the support to fix that. Kind Regards Dano

```html
<!DOCTYPE html>
<html lang="en">
<head>
<meta charset="utf-8">
<title>velmu GmbH – Business Cards</title>
<link rel="stylesheet" href="https://fonts.googleapis.com/css2?family=Questrial&family=Arimo:wght@400;700&display=swap">
<style>
  :root {
    --teal: #22545f;
    --rose: #d98782;
    --mauve: #a5716f;
    --paper: #ffffff;
    --ink: #111111;
    --stage: #e6e6e6;
  }
  * { margin: 0; padding: 0; box-sizing: border-box; }
  html, body { width: 1200px; height: 900px; overflow: hidden; background: var(--stage); }
  .sheet { position: relative; width: 1200px; height: 900px; }

  .card {
    position: absolute;
    left: 260px;
    width: 680px;
    height: 390px;
    background: var(--paper);
    overflow: hidden;
    box-shadow: 0 6px 18px rgba(0,0,0,0.18);
  }
  .card--back { top: 45px; }
  .card--front { top: 465px; }
  .card__art { position: absolute; inset: 0; width: 100%; height: 100%; }

  .brand {
    position: absolute;
    display: flex;
    align-items: center;
    font-family: "Questrial", sans-serif;
    font-weight: 400;
  }
  .brand__dot { border-radius: 50%; flex: none; }

  /* front side */
  .card--front .brand { left: 248px; top: 128px; gap: 18px; color: var(--teal); font-size: 96px; line-height: 1; letter-spacing: 4px; }
  .card--front .brand__dot { width: 62px; height: 62px; background: var(--teal); }
  .tagline {
    position: absolute;
    left: 250px; top: 250px;
    font-family: "Questrial", sans-serif;
    font-size: 38px;
    letter-spacing: 4px;
    color: var(--teal);
    white-space: nowrap;
  }

  /* back side */
  .card--back .brand { left: 34px; top: 270px; gap: 10px; color: var(--paper); font-size: 44px; line-height: 1; letter-spacing: 2px; }
  .card--back .brand__dot { width: 30px; height: 30px; background: var(--paper); }
  .contact {
    position: absolute;
    right: 40px; top: 40px;
    text-align: right;
    font-family: "Arimo", sans-serif;
    color: var(--ink);
    font-size: 20px;
    line-height: 1.3;
    white-space: nowrap;
  }
  .contact__name { font-weight: 700; font-size: 21px; margin-bottom: 16px; }
  .contact__address { margin-bottom: 16px; }
</style>
</head>
<body>
<main class="sheet">

  <section class="card card--back" aria-label="Business card, contact side">
    <svg class="card__art" viewBox="0 0 680 390" aria-hidden="true">
      <path fill="var(--teal)" d="M0 70 C150 90 250 180 320 255 C390 325 520 352 680 362 V390 H0 Z"/>
      <path fill="none" stroke="var(--mauve)" stroke-width="14" d="M0 52 C150 72 255 160 328 236 C398 306 525 334 680 344"/>
      <path fill="none" stroke="var(--rose)" stroke-width="8" d="M0 30 C155 50 262 138 338 214 C408 284 530 312 680 322"/>
    </svg>
    <div class="brand"><span class="brand__name">velmu</span><span class="brand__dot"></span></div>
    <div class="contact">
      <p class="contact__name">Lukas Ferrant</p>
      <p class="contact__address">Lindenhofweg 14<br>8045 Zürich</p>
      <p class="contact__phone">12 12 456 31 0041</p>
      <p class="contact__email">lukas.ferrant@postfeld.ch</p>
    </div>
  </section>

  <section class="card card--front" aria-label="Business card, brand side">
    <svg class="card__art" viewBox="0 0 680 390" aria-hidden="true">
      <path fill="var(--teal)" d="M0 0 H250 C205 60 130 100 108 190 C92 255 112 320 82 390 H0 Z"/>
      <circle cx="70" cy="50" r="120" fill="var(--paper)" opacity="0.12"/>
      <path fill="none" stroke="var(--mauve)" stroke-width="16" d="M262 -4 C217 58 142 100 120 190 C104 256 124 322 94 394"/>
      <path fill="none" stroke="var(--rose)" stroke-width="9" d="M290 -4 C245 60 170 102 148 192 C132 258 152 324 122 394"/>
    </svg>
    <div class="brand"><span class="brand__name">velmu</span><span class="brand__dot"></span></div>
    <p class="tagline">bright by nature</p>
  </section>

</main>
</body>
</html>
```